Moder Business Card Design for Renewables Business

Need a business card design for my business. We collect & repurpose spent coffee ground from cafes. The cards will be made from recycled paper. Needs to fit our corporate colour scheme of white, green & brown (see logo for colour codes). Eco friendly, modern, intresting & eye catching.
This card needs to convey the message of the business and fit into its mantra of eco-friendly, sustainable etc.

Target Market(s)

Cafe Owners, Coffee Drinkers, Recycling Companies, Farmers

Industry/Entity Type

Recycling

Contact Information for Business Card

Name; Peter Halloran
Phone; 0412 386 527
e-mail; info@lumatrove.com.au
website; www.lumatrove.com.au

Font styles to use
Sans Serif
Script

Colors

Designer to choose colors to be used in the design.

Requirements
Must have
• FRONT;
• Logo, Name (Peter Halloran), phone number, e-mail address, website
• BACK;
• On the back in cursive text; 'REVIVING VALUE IN EVERY SPENT CUP'
• Small facebook & Instagram logos with text 'Lumatrove'
Should not have
• messy design

```html
<!DOCTYPE html>
<html lang="en">
<head>
<meta charset="utf-8">
<title>Lumatrove business card</title>
<link rel="stylesheet" href="https://fonts.googleapis.com/css2?family=Arimo:ital,wght@0,400;0,700;1,700&display=swap">
<style>
  :root {
    --backdrop: #2b2b2b;
    --paper: #ffffff;
    --paper-shade: #eeeeee;
    --brown: #4a2410;
    --green: #6aa43a;
    --text-font: "Arimo", Arial, sans-serif;
  }
  * { box-sizing: border-box; margin: 0; padding: 0; }
  html, body {
    width: 1200px;
    height: 997px;
    overflow: hidden;
    background: var(--backdrop);
    font-family: var(--text-font);
  }
  .canvas {
    position: relative;
    width: 1200px;
    height: 997px;
  }
  .card {
    position: absolute;
    width: 540px;
    height: 330px;
    background: linear-gradient(135deg, var(--paper) 55%, var(--paper-shade));
    overflow: hidden;
  }

  /* Back of the card */
  .card-back { left: 60px; top: 130px; }
  .card-back .brand-block {
    position: absolute;
    left: 0; right: 0; top: 48px;
    display: flex;
    flex-direction: column;
    align-items: center;
  }
  .brand-mark {
    width: 110px;
    height: 110px;
    border-radius: 50%;
    border: 10px solid var(--brown);
    margin-bottom: 18px;
  }
  .brand-name {
    color: var(--green);
    font-weight: 700;
    font-size: 30px;
    letter-spacing: 1px;
    text-transform: uppercase;
  }
  .tagline {
    margin-top: 10px;
    color: var(--green);
    font-weight: 700;
    font-style: italic;
    font-size: 15px;
    letter-spacing: 0.5px;
  }
  .social {
    margin-top: 12px;
    display: flex;
    align-items: center;
    gap: 8px;
    color: var(--brown);
    font-weight: 700;
    font-size: 16px;
  }
  .social-square {
    width: 18px;
    height: 18px;
    background: var(--brown);
  }

  /* Front of the card */
  .card-front { left: 600px; top: 500px; }
  .card-front .brand-name {
    position: absolute;
    left: 34px;
    top: 92px;
    font-size: 29px;
  }
  .front-ring {
    position: absolute;
    left: 318px;
    top: -40px;
    width: 310px;
    height: 310px;
    border-radius: 50%;
    border: 14px solid var(--brown);
  }
  .person {
    position: absolute;
    left: 34px;
    top: 178px;
  }
  .person-name {
    color: var(--brown);
    font-weight: 700;
    font-size: 19px;
    text-transform: uppercase;
  }
  .person-role {
    color: var(--green);
    font-size: 15px;
    margin-top: 2px;
  }
  .contacts {
    position: absolute;
    left: 34px;
    top: 244px;
    list-style: none;
    color: var(--brown);
    font-size: 14px;
  }
  .contacts li {
    display: flex;
    align-items: center;
    gap: 8px;
    height: 22px;
  }
  .contact-icon {
    width: 16px;
    height: 16px;
    border-radius: 50%;
    background: var(--brown);
    display: flex;
    align-items: center;
    justify-content: center;
  }
  .contacts .website {
    font-weight: 700;
    letter-spacing: 1.5px;
    font-size: 14px;
    margin-top: 2px;
  }
</style>
</head>
<body>
<main class="canvas">

  <section class="card card-back" aria-label="Card back">
    <div class="brand-block">
      <div class="brand-mark"></div>
      <div class="brand-name">Lumatrove</div>
      <p class="tagline">‘REVIVING VALUE IN EVERY SPENT CUP’</p>
      <div class="social">
        <span class="social-square"></span>
        <span>Lumatrove</span>
      </div>
    </div>
  </section>

  <section class="card card-front" aria-label="Card front">
    <div class="front-ring"></div>
    <div class="brand-name">Lumatrove</div>
    <div class="person">
      <p class="person-name">Peter Halloran</p>
      <p class="person-role">Director</p>
    </div>
    <ul class="contacts">
      <li>
        <span class="contact-icon">
          <svg width="10" height="10" viewBox="0 0 10 10" aria-hidden="true">
            <path d="M2 1 L3.6 1 L4.2 3 L3.2 3.8 Q4 5.6 6.2 6.8 L7 5.8 L9 6.4 L9 8 Q8.6 9 7.4 9 Q1 8 1 2.4 Q1 1 2 1 Z" fill="#fff"/>
          </svg>
        </span>
        <span>0412 386 527</span>
      </li>
      <li>
        <span class="contact-icon">
          <svg width="10" height="10" viewBox="0 0 10 10" aria-hidden="true">
            <rect x="1" y="2.5" width="8" height="5.5" fill="none" stroke="#fff" stroke-width="1"/>
            <path d="M1 2.5 L5 5.8 L9 2.5" fill="none" stroke="#fff" stroke-width="1"/>
          </svg>
        </span>
        <span>info@lumatrove.com.au</span>
      </li>
      <li class="website">www.lumatrove.com.au</li>
    </ul>
  </section>

</main>
</body>
</html>
```